Inspirational Quote Poster for Employees

For this project, we need a simple yet high-impact poster template that will be customized for each of our employees with a personalized inspirational quote and color scheme. This template should allow us to quickly and easily customize the text and colors in the poster without a lot of effort.

The poster design should consist of:
- A stylized text area to contain the main text of the quote
- A separate text area to contain the source of quote
- A background that complements the color and style of the text

Text may use different typographic effects (such as color, stroke weight, italicization, font size changes, drop shadows) to draw attention to words in the quote; the source of the quote may be formatted the same as the main text of the quote, or may be formatted differently to distinguish it from the main quote.

The background may be simply a single color, subtle texture, gradients, halftone effects, or other color/texture effects may be used to complement the text.

Examples of the types of posters envisioned by this project:
- http://www.pinvelora.example/marcusdtelford/quillbase-job-1/

Sample quotes to use to build your poster - choose whichever one you want, but be certain that the poster design will handle both long and short quotes:
- "Happiness in intelligent people is the rarest thing I know" - Walden Prosket
- "Wanting to be someone else is a waste of the person you are." - Rolf Dintey
- "Experience is not what happens to you. It is what you do with what happens to you." - Ferris Mundell
- "Simplicity is the ultimate in sophistication." - Rinaldo de Pavesco
- "You will get all you want in life if you help enough other people get what they want." - Tad Pomfrey
- "Hell, there are no rules here — we're trying to accomplish something." - Gareth Vullane

Industry/Entity Type

Quote

Requirements
Must have
• Final deliverable must be:
• - Formatted for an 18” x 24” poster (in portrait orientation)
• - Delivered in Adobe InDesign, Adobe Illustrator, or Extended PostScript format
• - Use CMYK color mode
• - Be print-ready at 300dpi resolution
• - Include any fonts used in the template

```html
<!DOCTYPE html>
<html lang="en">
<head>
<meta charset="utf-8">
<title>Quote Poster — Walden Prosket</title>
<link href="https://fonts.googleapis.com/css2?family=Jost:wght@400&display=swap" rel="stylesheet">
<style>
  :root {
    --paper: #d9d9d9;
    --panel-top: #8c8c8c;
    --panel-mid: #6c6c6c;
    --panel-low: #3f3f3f;
    --panel-bottom: #383838;
    --quote-ink: #f1f1f1;
    --source-ink: #c9c9c9;
  }
  html, body {
    margin: 0;
    padding: 0;
    overflow: hidden;
  }
  .poster {
    position: relative;
    width: 849px;
    height: 1200px;
    background: var(--paper);
    overflow: hidden;
    font-family: "Jost", "Futura", sans-serif;
  }
  .poster__panel {
    position: absolute;
    left: 20px;
    top: 22px;
    width: 810px;
    height: 1158px;
    background: linear-gradient(
      to bottom,
      var(--panel-top) 0%,
      #7e7e7e 30%,
      var(--panel-mid) 46%,
      #505050 58%,
      var(--panel-low) 70%,
      var(--panel-bottom) 100%
    );
    box-shadow: 0 0 6px 2px rgba(120, 120, 120, 0.6);
  }
  .poster__grain {
    position: absolute;
    inset: 0;
    width: 849px;
    height: 1200px;
    opacity: 0.22;
    mix-blend-mode: overlay;
    pointer-events: none;
  }
  .quote {
    position: absolute;
    left: 0;
    width: 849px;
    top: 221px;
    margin: 0;
    text-align: center;
    color: var(--quote-ink);
    font-size: 92px;
    line-height: 107.5px;
    font-weight: 400;
    text-transform: uppercase;
    letter-spacing: -0.5px;
    padding-left: 18px;
    box-sizing: border-box;
  }
  .quote__source {
    position: absolute;
    left: 0;
    width: 849px;
    top: 876px;
    margin: 0;
    text-align: center;
    color: var(--source-ink);
    font-size: 25px;
    letter-spacing: 4.5px;
    text-transform: uppercase;
    font-weight: 400;
    padding-left: 8px;
    box-sizing: border-box;
  }
</style>
</head>
<body>
  <main class="poster">
    <div class="poster__panel"></div>

    <blockquote class="quote">“Happiness in<br>intelligent<br>people is the<br>rarest thing<br>I know”</blockquote>
    <p class="quote__source">Walden Prosket</p>

    <svg class="poster__grain" viewBox="0 0 849 1200" aria-hidden="true">
      <filter id="grain-noise">
        <feTurbulence type="fractalNoise" baseFrequency="0.9" numOctaves="3" stitchTiles="stitch"/>
        <feColorMatrix type="saturate" values="0"/>
      </filter>
      <rect width="849" height="1200" filter="url(#grain-noise)"/>
    </svg>
  </main>
</body>
</html>
```